Bold Plum

I am starting a sharpening service for knives, scissors, and garden tools. It's a sole proprietorship, so it's a small business. The business name is "Bolt Plum." A one or two-page website is fine. Ember Guild has created a logo for me. There should be pictures of the things I sharpen. There will also be a price list for sharpened items. My address is: 18392 Calloway Lane, Stevenson Ranch, CA 91307. Phone number is 661-555-0172

```html
<!DOCTYPE html>
<html lang="en">
<head>
<meta charset="utf-8">
<title>Bolt Plum – Professional Sharpening Pricing</title>
<link href="https://fonts.googleapis.com/css2?family=Archivo:wght@700;800;900&family=Work+Sans:wght@400;500;600;700&display=swap" rel="stylesheet">
<style>
:root{
  --blue:#1668e8;
  --blue-soft:#eef4fe;
  --ink:#0f1729;
  --text:#4a5566;
  --muted:#6b7280;
  --line:#e7eaf0;
  --bg:#f8f9fb;
  --white:#ffffff;
}
*{box-sizing:border-box;margin:0;padding:0}
html,body{width:879px;height:1200px;overflow:hidden}
body{background:var(--bg);font-family:"Work Sans",sans-serif;color:var(--ink);position:relative}
.site-header{height:47px;background:var(--white);border-bottom:1px solid var(--line);display:flex;align-items:center;padding:0 44px}
.brand{display:flex;align-items:center;gap:7px;font-family:"Archivo",sans-serif;font-weight:900;font-size:13px;color:var(--ink);letter-spacing:-.2px}
.brand-dot{width:14px;height:14px;border-radius:50%;background:var(--blue)}
.nav{display:flex;gap:22px;margin-left:auto;margin-right:auto;padding-left:110px;font-size:9.5px}
.nav a{color:var(--ink);text-decoration:none}
.nav a.active{color:var(--blue);font-weight:600;text-decoration:underline;text-underline-offset:3px}
.btn-book{background:var(--blue);color:#fff;font-size:9.5px;font-weight:700;padding:7px 14px;border-radius:4px}
.intro{position:absolute;left:44px;top:72px}
.intro h1{font-family:"Archivo",sans-serif;font-weight:900;font-size:33px;letter-spacing:-1.4px;line-height:40px}
.intro p{margin-top:10px;font-size:12.5px;line-height:19px;color:var(--text);width:470px}
.price-card{position:absolute;left:44px;width:518px;background:var(--white);border:1px solid var(--line);border-radius:6px;overflow:hidden}
.price-card.kitchen{top:190px}
.price-card.garden{top:445px}
.card-head{height:42px;background:var(--blue-soft);border-bottom:1px solid var(--line);display:flex;align-items:center;gap:8px;padding:0 17px;color:var(--blue);font-family:"Archivo",sans-serif;font-weight:800;font-size:12.5px}
.card-head svg{width:13px;height:13px}
table{width:100%;border-collapse:collapse}
th{font-size:7.5px;letter-spacing:.9px;font-weight:600;color:var(--text);text-align:left;height:28px;padding:0 16px;border-bottom:1px solid var(--line)}
td{height:39px;padding:0 16px;font-size:9px;border-bottom:1px solid var(--line);color:var(--text);letter-spacing:.2px}
tr:last-child td{border-bottom:none}
td.item{color:var(--ink);font-weight:500;letter-spacing:.1px}
th.price,td.price{text-align:right}
.tag{display:inline-block;background:var(--blue-soft);color:var(--blue);font-weight:700;font-size:7.8px;padding:3px 5px;border-radius:3px}
.kitchen .col1{width:140px}
.garden .col1{width:166px}
.steps-title{position:absolute;left:44px;top:718px;font-family:"Archivo",sans-serif;font-weight:800;font-size:15.5px}
.steps{position:absolute;left:44px;top:755px;display:flex;gap:17px}
.step{width:161px;height:171px;background:var(--white);border:1px solid var(--line);border-radius:6px;padding:16px 16px}
.step-icon{width:33px;height:33px;border-radius:50%;background:var(--blue);display:flex;align-items:center;justify-content:center}
.step-icon svg{width:15px;height:15px}
.step h3{margin-top:14px;font-size:12px;font-weight:600}
.step p{margin-top:10px;font-size:9px;line-height:13.7px;color:var(--text);letter-spacing:.2px}
.find-card{position:absolute;left:590px;top:190px;width:245px;height:424px;background:var(--white);border:1px solid var(--line);border-radius:6px;padding:17px 16px}
.find-card h2{font-family:"Archivo",sans-serif;font-weight:800;font-size:13px}
.info{display:flex;gap:10px;margin-top:13px}
.info svg{width:14px;height:14px;flex:none}
.info strong{display:block;font-size:9px;font-weight:600}
.info span{display:block;font-size:9px;line-height:14.5px;color:var(--text);letter-spacing:.2px}
.map{position:absolute;left:16px;top:200px;width:211px;height:207px;border:1px solid var(--line);border-radius:4px;overflow:hidden}
.map-area{height:177px;background:linear-gradient(160deg,#dbe8d4,#c9e0c1 55%,#d7e6d8)}
.map-link{height:30px;display:flex;align-items:center;justify-content:center;gap:6px;font-size:8px;font-weight:600;letter-spacing:.9px;color:var(--text);background:#fafbfc;border-top:1px solid var(--line)}
.mobile-card{position:absolute;left:590px;top:637px;width:245px;height:145px;background:var(--blue);border-radius:6px;padding:18px 16px;color:#fff}
.mobile-card h2{font-family:"Archivo",sans-serif;font-weight:800;font-size:12px}
.mobile-card p{margin-top:8px;font-size:9px;line-height:15.5px;color:#e4edff;letter-spacing:.2px}
.btn-inquire{margin-top:16px;background:#fff;color:var(--blue);border-radius:4px;height:25px;display:flex;align-items:center;justify-content:center;font-size:9px;font-weight:700}
.site-footer{position:absolute;left:0;top:971px;width:879px;height:229px;background:var(--bg);border-top:1px solid var(--line)}
.foot-col{position:absolute;top:38px}
.foot-about{left:44px;width:240px}
.foot-about p{margin-top:16px;font-size:9px;line-height:13.8px;color:var(--text);letter-spacing:.2px}
.foot-links{left:317px}
.foot-news{left:590px;width:245px}
.foot-col h4{font-size:8.5px;letter-spacing:1.6px;font-weight:600}
.foot-links a{display:block;margin-top:9px;font-size:9px;color:var(--text);text-decoration:none;letter-spacing:.3px}
.foot-links h4{margin-bottom:14px}
.foot-news p{margin-top:14px;font-size:7.5px;line-height:11px;color:var(--text)}
.news-form{display:flex;gap:6px;margin-top:12px}
.news-input{width:208px;height:27px;border:1px solid var(--line);border-radius:4px;background:#fff;font-size:9.5px;color:var(--text);display:flex;align-items:center;padding:0 9px}
.news-btn{width:31px;height:27px;border-radius:4px;background:var(--blue);display:flex;align-items:center;justify-content:center}
.foot-rule{position:absolute;left:44px;right:44px;top:162px;border-top:1px solid var(--line)}
.copyright{position:absolute;left:0;right:0;top:186px;text-align:center;font-size:7.5px;color:var(--muted)}
</style>
</head>
<body>
<header class="site-header">
  <div class="brand"><span class="brand-dot"></span>BOLT PLUM</div>
  <nav class="nav">
    <a href="#">Home</a><a href="#">Services</a><a href="#" class="active">Pricing</a><a href="#">How it Works</a><a href="#">Contact</a>
  </nav>
  <div class="btn-book">Book Now</div>
</header>

<section class="intro">
  <h1>Professional Sharpening Pricing</h1>
  <p>Restoring factory edges to your most essential tools in Stevenson Ranch. Precision sharpening for kitchen, garden, and craft equipment.</p>
</section>

<section class="price-card kitchen">
  <div class="card-head">
    <svg viewBox="0 0 14 14" fill="none" stroke="currentColor" stroke-width="1.6" stroke-linecap="round"><path d="M3 1v4.5a1.5 1.5 0 0 0 3 0V1M4.5 1v12M10 13V1c1.6 1 2 3 2 5h-2"/></svg>
    Kitchen &amp; Culinary
  </div>
  <table>
    <tr><th class="col1">SERVICE ITEM</th><th>DETAILS</th><th class="price">PRICE</th></tr>
    <tr><td class="item">Kitchen Knives</td><td>Standard sharpening (straight edge)</td><td class="price"><span class="tag">$1.50/inch</span></td></tr>
    <tr><td class="item">Serrated Knives</td><td>Bread and steak knives</td><td class="price"><span class="tag">$2.00/inch</span></td></tr>
    <tr><td class="item">Pocket Knives</td><td>Single or multi-blade folding knives</td><td class="price"><span class="tag">From $8.00</span></td></tr>
    <tr><td class="item">Cleavers &amp; Axes</td><td>Heavy duty edge restoration</td><td class="price"><span class="tag">$15.00</span></td></tr>
  </table>
</section>

<section class="price-card garden">
  <div class="card-head">
    <svg viewBox="0 0 14 14"><rect x="1" y="1" width="12" height="12" rx="2" fill="currentColor"/><circle cx="7" cy="6" r="2.2" fill="#fff"/><path d="M7 8.5v3" stroke="#fff" stroke-width="1.3"/></svg>
    Garden &amp; Workshop
  </div>
  <table>
    <tr><th class="col1">SERVICE ITEM</th><th>DETAILS</th><th class="price">PRICE</th></tr>
    <tr><td class="item">Garden Shears</td><td>Pruners and hand shears</td><td class="price"><span class="tag">$12.00</span></td></tr>
    <tr><td class="item">Loppers</td><td>Bypass or anvil loppers</td><td class="price"><span class="tag">$15.00</span></td></tr>
    <tr><td class="item">Mower Blades</td><td>Sharpening and balancing</td><td class="price"><span class="tag">$20.00</span></td></tr>
    <tr><td class="item">Sewing Scissors</td><td>Fabric and craft shears</td><td class="price"><span class="tag">$12.00</span></td></tr>
  </table>
</section>

<h2 class="steps-title">How It Works</h2>
<section class="steps">
  <article class="step">
    <div class="step-icon"><svg viewBox="0 0 16 16"><path d="M8 1a5 5 0 0 0-5 5c0 3.8 5 9 5 9s5-5.2 5-9a5 5 0 0 0-5-5z" fill="#fff"/><circle cx="8" cy="6" r="1.8" fill="#1668e8"/></svg></div>
    <h3>1. Drop-off</h3>
    <p>Bring your dull tools to our Stevenson Ranch workshop during business hours. No appointment needed for drop-offs.</p>
  </article>
  <article class="step">
    <div class="step-icon"><svg viewBox="0 0 16 16" stroke="#fff" stroke-width="1.6" stroke-linecap="round" fill="#fff"><path d="M3 13l7-7"/><path d="M11 1v3M9.5 2.5h3M14 6v2M13 7h2M6 2v2M5 3h2" stroke-width="1.1"/></svg></div>
    <h3>2. Expert Care</h3>
    <p>Our professionals sharpen, hone, and polish each item using precision water-cooled equipment to protect the temper.</p>
  </article>
  <article class="step">
    <div class="step-icon"><svg viewBox="0 0 16 16" fill="#fff"><path d="M8 2a4 4 0 0 0-4 4v3.5L2.5 12h11L12 9.5V6a4 4 0 0 0-4-4z"/><circle cx="8" cy="13.5" r="1.5"/></svg></div>
    <h3>3. Ready for Pickup</h3>
    <p>Most orders are completed within 24-48 hours. We'll text or call you the moment your tools are sharp and ready.</p>
  </article>
</section>

<aside class="find-card">
  <h2>Find Us</h2>
  <div class="info" style="margin-top:15px">
    <svg viewBox="0 0 16 16"><path d="M8 1a5 5 0 0 0-5 5c0 3.8 5 9 5 9s5-5.2 5-9a5 5 0 0 0-5-5z" fill="#1668e8"/><circle cx="8" cy="6" r="1.8" fill="#fff"/></svg>
    <div><strong>Address</strong><span>18392 Calloway Lane</span><span style="margin-top:2px">Stevenson Ranch, CA 91307</span></div>
  </div>
  <div class="info">
    <svg viewBox="0 0 16 16"><path d="M3 1.5l3 .5 1 3-1.8 1.3a9 9 0 0 0 4.5 4.5L11 9l3 1 .5 3c-.5 1-1.5 1.5-2.5 1.5C6.5 14 2 9.5 1.5 4c0-1 .5-2 1.5-2.5z" fill="#1668e8"/></svg>
    <div><strong>Phone</strong><span>661-555-0172</span></div>
  </div>
  <div class="info">
    <svg viewBox="0 0 16 16"><circle cx="8" cy="8" r="7" fill="#1668e8"/><path d="M8 4v4.3l2.5 1.7" stroke="#fff" stroke-width="1.5" fill="none" stroke-linecap="round"/></svg>
    <div><strong>Hours</strong><span>Mon-Fri: 9am - 6pm</span><span>Sat: 10am - 4pm</span></div>
  </div>
  <div class="map">
    <div class="map-area" role="img" aria-label="Area map showing the Bolt Plum workshop location"></div>
    <div class="map-link"><svg width="9" height="9" viewBox="0 0 10 10"><path d="M5 0l5 5-5 5-5-5z" fill="#4a5566"/><path d="M3.5 6V4.5h3M5.5 3.3l1.2 1.2-1.2 1.2" stroke="#fff" stroke-width=".9" fill="none"/></svg>GET DIRECTIONS</div>
  </div>
</aside>

<aside class="mobile-card">
  <h2>Mobile Service Available</h2>
  <p>Need us to come to you? We offer on-site sharpening for residential and commercial kitchens (5+ item minimum).</p>
  <div class="btn-inquire">Inquire About Mobile</div>
</aside>

<footer class="site-footer">
  <div class="foot-col foot-about">
    <div class="brand"><span class="brand-dot"></span>BOLT PLUM</div>
    <p>Professional tool and knife sharpening specialists serving the Stevenson Ranch community with precision and care.</p>
  </div>
  <div class="foot-col foot-links">
    <h4>QUICK LINKS</h4>
    <a href="#">Service Guarantee</a><a href="#">Commercial Partners</a><a href="#">Gift Certificates</a><a href="#">Privacy Policy</a>
  </div>
  <div class="foot-col foot-news">
    <h4>NEWSLETTER</h4>
    <p>Get sharpening tips and seasonal garden tool maintenance reminders.</p>
    <div class="news-form">
      <div class="news-input">Email address</div>
      <div class="news-btn"><svg width="9" height="9" viewBox="0 0 10 10"><path d="M1 1l8 4-8 4 1.5-4z" fill="#fff"/></svg></div>
    </div>
  </div>
  <div class="foot-rule"></div>
  <div class="copyright">© 2024 Bolt Plum Professional Services. All rights reserved. Precision edges since 2018.</div>
</footer>
</body>
</html>
```